Refreshed PPT Presentation for US based firms

There are basically 4 types of slides in this presentation:
* Roadmap (Title, Agenda, Billboards)
* Teaching (Content, Examples)
* Samples (Real life samples)
* Polls (Placeholders for interactive polls)
We want new templates for each of these types of templates with coordinated graphics, images, icons and fonts.

```html
<!DOCTYPE html>
<html lang="en">
<head>
<meta charset="utf-8">
<title>Advice and Counsel Through Email</title>
<link href="https://fonts.googleapis.com/css2?family=Poppins:wght@400;500;600;700;800;900&display=swap" rel="stylesheet">
<style>
:root{
  --pink:#e0309a;
  --pink-soft:#f07ab9;
  --ink:#1c1c1c;
  --text:#333333;
  --grey-band:#dedede;
  --page:#f4f4f4;
  --white:#ffffff;
  --dark-photo:#3a3a3e;
}
*{box-sizing:border-box;margin:0;padding:0}
html,body{width:1200px;height:4084px;overflow:hidden;background:var(--page)}
body{position:relative;font-family:'Poppins',sans-serif;color:var(--text)}
.slide{position:absolute;left:51px;width:1097px;height:617px;overflow:hidden;background:var(--white);box-shadow:0 1px 3px rgba(0,0,0,.08)}
.abs{position:absolute}
.photo{position:absolute}
.shape{position:absolute;left:0;top:0;width:100%;height:100%}
.frame{position:absolute;border:2px solid var(--ink)}
.frame-light{position:absolute;border:2px solid rgba(255,255,255,.85)}
.kicker{font-weight:700;color:var(--pink);font-size:25px}
.headline{font-weight:800;text-transform:uppercase;line-height:1.1}
.btn{position:absolute;background:var(--pink);color:var(--white);font-weight:700;font-size:18px;padding:6px 11px}
.bullets{list-style:none}
.bullets li{position:relative}
.dot{position:absolute;width:16px;height:16px;border-radius:50%;background:var(--pink)}
.ring{position:absolute;width:16px;height:16px;border-radius:50%;border:2px solid var(--pink)}
.tile{position:absolute;background:var(--white);padding:4px;box-shadow:0 2px 6px rgba(0,0,0,.25)}
.tile div{width:100%;height:100%}
.footer{position:absolute;top:4040px;font-size:11px;color:#555}
</style>
</head>
<body>

<!-- Title slide -->
<section class="slide" style="top:51px">
  <div class="photo" role="img" aria-label="Colleagues in discussion at a meeting table with a laptop" style="inset:0;background:linear-gradient(110deg,#2e2a2a 0%,#5a4c46 45%,#3d3f47 100%)"></div>
  <svg class="shape" viewBox="0 0 1097 617" preserveAspectRatio="none">
    <polygon points="840,0 869,0 980,617 950,617" fill="rgba(200,200,200,.55)"/>
    <polygon points="869,0 1097,0 1097,617 980,617" fill="var(--pink)"/>
  </svg>
  <div class="frame-light" style="left:20px;top:20px;width:1012px;height:577px"></div>
  <div class="abs kicker" style="left:71px;top:58px">Advice and Counsel</div>
  <h1 class="abs headline" style="left:63px;top:198px;font-size:46px;color:var(--white)">Advice and Counsel<br>Through Email</h1>
  <div class="abs" style="left:67px;top:340px;font-size:18px;font-weight:700;color:var(--white)">DANA WHITFIELD FOR NORTHGATE LAW GROUP P.C.</div>
  <div class="btn" style="left:62px;top:406px">Go to www.pollhub.net/danawhitfield412</div>
</section>

<!-- Agenda slide -->
<section class="slide" style="top:715px">
  <div class="photo" role="img" aria-label="Group of people seated in a circle talking" style="inset:0;clip-path:polygon(0 0,599px 0,401px 100%,0 100%);background:linear-gradient(160deg,#e8e4dc 0%,#b59a80 55%,#6b5442 100%)"></div>
  <svg class="shape" viewBox="0 0 1097 617" preserveAspectRatio="none">
    <polygon points="599,0 639,0 441,617 401,617" fill="var(--pink)"/>
  </svg>
  <div class="frame" style="left:430px;top:24px;width:641px;height:572px;border-left:none"></div>
  <h2 class="abs headline" style="left:607px;top:112px;font-size:48px;color:var(--pink)">Agenda</h2>
  <ul class="bullets abs" style="left:607px;top:196px;font-size:17px;font-weight:700;color:var(--ink)">
    <li style="height:50px"><span class="dot" style="left:0;top:4px"></span><span style="margin-left:40px">Preparation and process</span></li>
    <li style="height:50px"><span class="dot" style="left:0;top:4px"></span><span style="margin-left:40px">Audience and purpose</span></li>
    <li style="height:50px"><span class="dot" style="left:0;top:4px"></span><span style="margin-left:40px">Characteristics of a quality response</span></li>
    <li style="height:50px"><span class="dot" style="left:0;top:4px"></span><span style="margin-left:40px">Quick</span></li>
    <li style="height:50px"><span class="dot" style="left:0;top:4px"></span><span style="margin-left:40px">Clear</span></li>
    <li style="height:50px"><span class="dot" style="left:0;top:4px"></span><span style="margin-left:40px">Concise</span></li>
  </ul>
</section>

<!-- Writing process slide -->
<section class="slide" style="top:1381px">
  <div class="frame" style="left:29px;top:230px;width:1040px;height:364px"></div>
  <div class="photo" role="img" aria-label="Gavel and scales of justice on a desk" style="left:0;top:0;width:1097px;height:330px;clip-path:polygon(0 0,1097px 0,1097px 205px,0 311px);background:linear-gradient(90deg,var(--pink) 0%,var(--pink) 45%,#e986b4 60%,#c7a08c 80%,#8a6a55 100%)"></div>
  <svg class="shape" viewBox="0 0 1097 617" preserveAspectRatio="none">
    <polygon points="0,311 1097,205 1097,225 0,331" fill="var(--grey-band)"/>
  </svg>
  <h2 class="abs headline" style="left:89px;top:80px;font-size:44px;color:var(--white)">Four Stages of the<br>Writing Process</h2>
  <div class="abs" style="left:89px;top:344px;font-size:17px;line-height:1;color:var(--text)">
    <p style="height:50px">Madman, the creative force who generates the ideas</p>
    <p style="height:50px">Architect, the planner who builds the structure for the document</p>
    <p style="height:50px">Carpenter, the craftsman who writes a draft</p>
    <p>Judge, the reviewer who edits the draft</p>
  </div>
  <div class="tile" style="left:854px;top:19px;width:178px;height:135px"><div role="img" aria-label="Sketched idea bubbles around a light bulb" style="background:linear-gradient(135deg,#f2f2f2,#d8d8d8 60%,#f3c62a)"></div></div>
  <div class="tile" style="left:675px;top:160px;width:178px;height:135px"><div role="img" aria-label="Wooden gavel on its block" style="background:linear-gradient(160deg,#ffffff 30%,#a0623a 70%,#6e3f22)"></div></div>
  <div class="tile" style="left:859px;top:295px;width:179px;height:136px"><div role="img" aria-label="Architect working on a building model" style="background:linear-gradient(140deg,#3d4a56,#c49a70 60%,#e3c49c)"></div></div>
  <div class="tile" style="left:680px;top:441px;width:179px;height:134px"><div role="img" aria-label="Claw hammer" style="background:linear-gradient(160deg,#ffffff 30%,#8c8c8c 50%,#d9a066 75%)"></div></div>
</section>

<!-- Clarify slide -->
<section class="slide" style="top:2058px">
  <div class="frame" style="left:29px;top:24px;width:1040px;height:570px"></div>
  <div class="photo" role="img" aria-label="Smiling woman with glasses talking on a desk phone" style="inset:0;clip-path:polygon(647px 0,1097px 0,1097px 100%,837px 100%);background:linear-gradient(120deg,#efe9e2 0%,#cdb49a 45%,#8d8f92 100%)"></div>
  <svg class="shape" viewBox="0 0 1097 617" preserveAspectRatio="none">
    <polygon points="615,0 647,0 837,617 805,617" fill="var(--pink)"/>
  </svg>
  <h2 class="abs headline" style="left:62px;top:86px;font-size:46px;color:var(--pink)">Clarify the<br>Question &amp; the Timing</h2>
  <div class="abs" style="left:0;top:0;font-size:17px;color:var(--text)">
    <span class="dot" style="left:65px;top:226px"></span><span class="abs" style="left:90px;top:222px;white-space:nowrap">Sometimes a little clarity is required</span>
    <span class="dot" style="left:65px;top:276px"></span><span class="abs" style="left:90px;top:272px;white-space:nowrap">Seek clarity in, egads, a phone call or a short email</span>
    <span class="dot" style="left:65px;top:326px"></span><span class="abs" style="left:90px;top:322px;white-space:nowrap">Then confirm the scope of the inquiry in an email</span>
    <span class="ring" style="left:97px;top:383px"></span><span class="abs" style="left:136px;top:380px;white-space:nowrap">In scope: Address ability to restrict marijuana use in six states</span>
    <span class="ring" style="left:97px;top:434px"></span><span class="abs" style="left:136px;top:431px;width:590px;line-height:1.45">Out of scope: consequences of past practices in compliance department</span>
    <span class="ring" style="left:97px;top:510px"></span><span class="abs" style="left:136px;top:507px">Timing</span>
  </div>
</section>

<!-- Skills slide -->
<section class="slide" style="top:2728px">
  <div class="frame" style="left:29px;top:240px;width:1040px;height:353px"></div>
  <div class="photo" role="img" aria-label="Smiling professional woman in an office" style="left:0;top:0;width:1097px;height:340px;clip-path:polygon(0 0,1097px 0,1097px 331px,0 228px);background:linear-gradient(90deg,#cfd6d8 0%,#8c7a68 22%,#c9c4bd 42%,var(--pink) 60%,var(--pink) 100%)"></div>
  <svg class="shape" viewBox="0 0 1097 617" preserveAspectRatio="none">
    <polygon points="0,228 1097,331 1097,351 0,248" fill="var(--grey-band)"/>
  </svg>
  <h2 class="abs headline" style="right:111px;top:90px;font-size:46px;color:var(--white);text-align:right">Three Skills<br>Involved</h2>
  <div class="photo" role="img" aria-label="Profile of a head made of colourful puzzle pieces" style="left:36px;top:300px;width:571px;height:285px;background:radial-gradient(ellipse at 40% 50%,#f4a940 0%,#d9478a 25%,#4a8fd4 45%,#f7f7f7 70%,#ffffff 100%)"></div>
  <div class="abs" style="right:120px;top:364px;width:320px;text-align:right;font-size:17px;line-height:1.45;color:var(--text)">
    <p style="margin-bottom:26px">Identifying a sentence that can be improved</p>
    <p style="margin-bottom:26px">Identifying the problem</p>
    <p>Revising the sentence</p>
  </div>
</section>

<!-- Closing slide -->
<section class="slide" style="top:3402px">
  <div class="photo" role="img" aria-label="Audience seated in a room, shown in dark tones" style="inset:0;background:linear-gradient(100deg,#4b4b4f 0%,#2f2f33 50%,#1a1a1c 100%)"></div>
  <svg class="shape" viewBox="0 0 1097 617" preserveAspectRatio="none">
    <polygon points="254,0 284,0 93,617 63,617" fill="rgba(200,200,200,.55)"/>
    <polygon points="0,0 254,0 63,617 0,617" fill="var(--pink)"/>
  </svg>
  <div class="frame-light" style="left:64px;top:22px;width:1013px;height:575px;border-left:none"></div>
  <div class="abs" style="right:98px;top:56px;font-size:26px;font-weight:700;color:var(--white)">Advice and Counsel</div>
  <div class="abs headline" style="right:96px;top:222px;font-size:118px;font-weight:900;color:var(--white);letter-spacing:-1px;line-height:1">Thank You</div>
  <div class="btn" style="right:98px;top:374px">Go to www.pollhub.net/danawhitfield412</div>
</section>

<div class="footer" style="left:51px">© 2023 &nbsp;Advice and Counsel</div>
<div class="footer" style="right:55px">C64</div>

</body>
</html>
```